Simple+Professional tech feel + warm and friendly box design for pet test kit

Project Name: 10-Minute Canine & Feline Rapid Test Kit Packaging Design
Target Brand Reference: VETRALUX (South Korea) styles
Design Style Direction: Professional tech feel + warm and friendly
Professionalism (Professional): Clear typography and distinct information hierarchy to reflect the product’s scientific rigor and accuracy.
Technological: Reflected through clean graphics and a minimalist layout.
Friendly: Utilise soft, warm colour combinations to convey care for pets and well-wishes for their health.
International: The design should align with mainstream aesthetics and avoid cultural ambiguities.

Target Market(s)
European Union and the United States
Industry/Entity Type
Veterinary Medical
Look and feel
Each slider illustrates characteristics of the customer's brand and the style your logo design should communicate.

```html
<!DOCTYPE html>
<html lang="en">
<head>
<meta charset="utf-8">
<title>ClaroVet Canine &amp; Feline Rapid Test Kit – Packaging</title>
<link href="https://fonts.googleapis.com/css2?family=DM+Sans:wght@400;500;600;700&display=swap" rel="stylesheet">
<style>
  :root {
    --backdrop: #dedede;
    --white: #fbfbfb;
    --teal: #1fada3;
    --teal-deep: #15968d;
    --orange: #f0921e;
    --ink-grey: #5b5f66;
    --ink-dark: #2b2d30;
  }
  * { box-sizing: border-box; margin: 0; padding: 0; }
  html, body {
    width: 1200px; height: 701px; overflow: hidden;
    background: var(--backdrop);
    font-family: "DM Sans", sans-serif;
  }
  .packaging {
    position: absolute; left: 170px; top: 150px;
    display: flex; height: 400px;
  }
  /* side panel */
  .side-panel {
    width: 190px; height: 100%;
    display: flex; flex-direction: column;
  }
  .side-panel__top {
    flex: 0 0 230px; background: var(--teal-deep);
    padding: 26px 20px; color: var(--white);
    display: flex; flex-direction: column; justify-content: space-between;
  }
  .side-panel__brand { font-size: 22px; font-weight: 600; }
  .side-panel__tagline { font-size: 10.5px; line-height: 1.45; font-weight: 500; }
  .side-panel__band { flex: 0 0 7px; background: var(--orange); }
  .side-panel__info {
    flex: 1; background: var(--white); padding: 14px 20px;
    font-size: 7.5px; line-height: 1.6; color: var(--ink-dark);
  }
  .side-panel__note { margin-top: 6px; }
  /* front panel */
  .front-panel {
    width: 650px; height: 100%; position: relative;
    display: flex; flex-direction: column;
  }
  .front-panel__header {
    flex: 0 0 170px; background: var(--white); position: relative;
  }
  .maker-name {
    position: absolute; right: 26px; top: 22px;
    font-size: 20px; font-weight: 500; color: var(--ink-dark);
  }
  .product-brand {
    position: absolute; left: 38px; top: 72px;
    display: flex; align-items: center; gap: 12px;
    font-size: 60px; font-weight: 700; letter-spacing: -1px;
    color: var(--teal); line-height: 1;
  }
  .product-brand__dot {
    width: 16px; height: 16px; border-radius: 50%; background: var(--orange);
  }
  .product-brand__tm {
    font-size: 13px; font-weight: 500; color: var(--ink-grey);
    align-self: flex-start; margin-left: -6px;
  }
  .front-panel__band { flex: 0 0 9px; background: var(--orange); }
  .front-panel__body {
    flex: 1; background: var(--teal); position: relative; color: var(--white);
    padding: 30px 36px;
  }
  .product-title { font-size: 29px; font-weight: 600; line-height: 1.25; }
  .product-species { margin-top: 14px; font-size: 19px; font-weight: 400; }
  .test-count {
    position: absolute; left: 36px; bottom: 26px;
    background: var(--orange); border-radius: 16px;
    padding: 5px 14px; font-size: 17px; font-weight: 500;
  }
  .pet-illustration {
    position: absolute; right: 30px; bottom: 18px;
    width: 180px; height: 175px; border-radius: 14px;
    background: linear-gradient(160deg, rgba(255,255,255,0.22), rgba(255,255,255,0.08));
  }
</style>
</head>
<body>
  <main class="packaging">
    <section class="side-panel">
      <div class="side-panel__top">
        <div class="side-panel__brand">ClaroVet™</div>
        <p class="side-panel__tagline">A Clear View into Pet Health |<br>Made by Norvik</p>
      </div>
      <div class="side-panel__band"></div>
      <div class="side-panel__info">
        <p>Norvik Biotech Limited</p>
        <p>Web: www.norvik-bio.example</p>
        <p>E-mail: sales@norvik-bio.example</p>
        <p class="side-panel__note">(For accurate results, please read the instructions carefully before use)</p>
      </div>
    </section>

    <section class="front-panel">
      <header class="front-panel__header">
        <div class="maker-name">Norvik</div>
        <div class="product-brand">
          <span class="product-brand__dot"></span>
          <span>ClaroVet</span>
          <span class="product-brand__tm">TM</span>
        </div>
      </header>
      <div class="front-panel__band"></div>
      <div class="front-panel__body">
        <h1 class="product-title">10-minute Canine<br>&amp; Feline Rapid Test Kit</h1>
        <p class="product-species">For Dogs and Cats</p>
        <span class="test-count">5 Tests/Kit</span>
        <div class="pet-illustration" role="img" aria-label="White line illustration of a dog and a cat sitting side by side"></div>
      </div>
    </section>
  </main>
</body>
</html>
```